Weightloss company needs Business Card

We want a business card that is clean and professional, yet portrays that we are a friendly, innovative, and versatile program designed to fit the needs of our clients.
I would like there to be 2 sides, one side having an appointment card, and the other side containing the logo and business information. There can be decorations on both sides. The logo is attached.

Target Market(s)

Men and women 40-60

Industry/Entity Type

Business

Contact Information for Business Card

Font styles to use
Sans Serif

Requirements
Must have
• The logo, space for business information
Nice to have
• The colors in the logo
Should not have
• No pictures of people or food

```html
<!DOCTYPE html>
<html lang="en">
<head>
<meta charset="utf-8">
<title>Renew Turn Wellness – Business Card</title>
<link rel="stylesheet" href="https://fonts.googleapis.com/css2?family=Lato:wght@400;700;900&display=swap">
<style>
  :root {
    --backdrop: #a31f24;
    --card: #ffffff;
    --brand-red: #e8202f;
    --ink: #111111;
    --sky: #4fc3ea;
    --text-grey: #6d6d6d;
    --band-grey: #f1f2f4;
    --rule: #222222;
  }
  * { box-sizing: border-box; margin: 0; padding: 0; }
  html, body {
    width: 1200px;
    height: 800px;
    overflow: hidden;
  }
  body {
    background: var(--backdrop);
    font-family: "Lato", Arial, sans-serif;
    position: relative;
  }
  .card {
    position: absolute;
    top: 250px;
    width: 525px;
    height: 300px;
    background: var(--card);
    box-shadow: 0 6px 18px rgba(0,0,0,0.35);
    overflow: hidden;
  }
  .card--front { left: 50px; }
  .card--back { left: 625px; }

  .accent-area {
    position: absolute;
    background: linear-gradient(135deg, var(--ink) 0%, var(--brand-red) 55%, var(--sky) 100%);
    opacity: 0.9;
  }
  .card--front .accent-area { left: 360px; top: 28px; width: 165px; height: 144px; }
  .card--back .accent-area { left: 0; top: 128px; width: 195px; height: 144px; }

  .brand {
    position: absolute;
    display: flex;
    align-items: center;
    gap: 8px;
    color: var(--brand-red);
    font-weight: 900;
    font-size: 24px;
    line-height: 1;
    white-space: nowrap;
  }
  .brand__dot {
    width: 14px;
    height: 14px;
    border-radius: 50%;
    background: var(--brand-red);
    flex: none;
  }
  .card--front .brand { left: 48px; top: 94px; }

  .contact {
    position: absolute;
    left: 48px;
    top: 150px;
    color: var(--text-grey);
  }
  .contact__name {
    color: var(--brand-red);
    font-size: 22px;
    font-weight: 400;
    margin-bottom: 2px;
  }
  .contact__role { font-size: 12px; margin-bottom: 8px; }
  .contact__line { font-size: 13.5px; line-height: 1.45; }

  .card--back .brand { right: 40px; top: 60px; }
  .appointment__title {
    position: absolute;
    right: 120px;
    top: 118px;
    color: var(--brand-red);
    font-size: 21px;
  }
  .field {
    position: absolute;
    display: flex;
    align-items: flex-end;
    gap: 8px;
    font-size: 16px;
    color: var(--ink);
  }
  .field__rule {
    display: inline-block;
    border-bottom: 1.5px solid var(--rule);
    margin-bottom: 4px;
  }
  .field--time { right: 28px; top: 150px; }
  .field--time .field__rule { width: 110px; }
  .date-band {
    position: absolute;
    left: 195px;
    right: 0;
    top: 190px;
    height: 40px;
    background: var(--band-grey);
  }
  .field--date { left: 215px; top: 198px; }
  .field--date .field__rule { width: 190px; }
</style>
</head>
<body>

<section class="card card--front" aria-label="Card front with contact details">
  <div class="accent-area" role="img" aria-label="Decorative stepped pattern in black, red and blue"></div>
  <div class="brand"><span class="brand__dot"></span>Renew Turn Wellness</div>
  <div class="contact">
    <p class="contact__name">Sam Porter</p>
    <p class="contact__role">Manager</p>
    <p class="contact__line">555 010 2468</p>
    <p class="contact__line">www.renewturnsite.com</p>
    <p class="contact__line">samporter@email.com</p>
  </div>
</section>

<section class="card card--back" aria-label="Card back with appointment form">
  <div class="date-band"></div>
  <div class="accent-area" role="img" aria-label="Decorative stepped pattern in black, red and blue"></div>
  <div class="brand"><span class="brand__dot"></span>Renew Turn Wellness</div>
  <p class="appointment__title">Appointment</p>
  <p class="field field--time">Time <span class="field__rule"></span></p>
  <p class="field field--date">Date <span class="field__rule"></span></p>
</section>

</body>
</html>
```